Web Page Design for a Website that Provides Tutoring

I am looking to create an online tutoring website. The website will allow parents or students to contact tutors with a view to instructing them to tutor themselves or their children.

The name of the website is LendYourLessons.

This brief is to create the design for one of the web pages for this web site. I am hoping the same designer will be available to design other pages.

The page I want designed is one of the more complex and I have attached the design as an excel spreadsheet. The web page needs to include all the items on this page but if you want to change the positioning of the items then Im fine with that.

I recently had two logos created for this website. My favourite is the one with a mortar board but im not sure I like the colours. I have attached both of these logos and you can use either of them, change the colours or create something different. I just want a design pleasing to the eye. If the logo is changed I would like that in a seperate file.

So can you please submit designs for this page. I have attached the two logos which you can use, change or if you feel you have a better idea then you can use that.

On the spreadsheet the Send Message, Favourite etc are buttons.

Target Market(s)

People who want to better themselves.
Possible middle class to upper class.

Industry/Entity Type

Tutoring

Number of Pages Required

1 page

Requirements
Must have
• The designs must have alot of the information attached in the spreadsheet.

```html
<!DOCTYPE html>
<html lang="en">
<head>
<meta charset="utf-8">
<title>LendYourLessons – Tutor Profile</title>
<link href="https://fonts.googleapis.com/css2?family=Varela+Round&family=Nunito:wght@300;400&display=swap" rel="stylesheet">
<style>
  :root {
    --orange: #f7941d;
    --blue: #00aeef;
    --text: #555559;
    --muted: #9a9aa0;
    --hero-bg: #f6f6fb;
    --pill-bg: #f1f1f7;
    --line: #ececf0;
    --footer-bg: #3e3e42;
    --white: #ffffff;
  }
  * { box-sizing: border-box; margin: 0; padding: 0; }
  html, body { width: 1200px; height: 971px; overflow: hidden; background: var(--white); }
  body { position: relative; font-family: "Varela Round", sans-serif; color: var(--text); }

  .site-header { position: absolute; top: 0; left: 0; width: 1200px; height: 72px; background: var(--white); border-bottom: 2px solid #ededf2; z-index: 3; }
  .brand { position: absolute; left: 210px; top: 14px; display: flex; align-items: center; gap: 8px; }
  .brand-dot { width: 14px; height: 14px; border-radius: 50%; background: var(--orange); }
  .brand-name { font-size: 31px; color: var(--orange); letter-spacing: -0.5px; }
  .account-links { position: absolute; left: 898px; top: 7px; font-size: 11px; color: var(--muted); font-family: "Nunito", sans-serif; }
  .account-links span { margin: 0 6px; }
  .main-nav { position: absolute; left: 626px; top: 36px; display: flex; gap: 14px; font-size: 14px; }
  .search-box { position: absolute; left: 904px; top: 33px; width: 87px; height: 25px; border: 2px solid #ececf0; border-radius: 13px; font-size: 10px; color: #b8b8be; padding: 5px 0 0 33px; }
  .search-box svg { position: absolute; left: 13px; top: 6px; }

  .hero { position: absolute; top: 72px; left: 0; width: 1200px; height: 406px; background: var(--hero-bg); overflow: hidden; }
  .hero-ring { position: absolute; left: 264px; top: -36px; width: 438px; height: 438px; border-radius: 50%; background: var(--orange); }
  .hero-photo { position: absolute; left: 258px; top: -41px; width: 438px; height: 438px; border-radius: 50%; background: radial-gradient(circle at 55% 45%, #d9c2ad 0%, #b69b86 22%, #6f7f9f 48%, #3f5787 70%, #8a8580 100%); }
  .accent-circle { position: absolute; left: 852px; top: -8px; width: 156px; height: 156px; border-radius: 50%; background: var(--blue); }
  .intro-card { position: absolute; left: 655px; top: 70px; width: 288px; height: 220px; background: var(--white); border-radius: 16px; box-shadow: 0 2px 10px rgba(0,0,0,0.06); padding: 30px 20px 0 20px; }
  .intro-card::before { content: ""; position: absolute; left: -21px; top: 44px; border: 11px solid transparent; border-right: 12px solid var(--white); }
  .intro-title { font-size: 18px; line-height: 20px; color: #5a5a5e; font-weight: normal; }
  .intro-text { margin-top: 8px; font-family: "Nunito", sans-serif; font-weight: 300; font-size: 11.5px; line-height: 19px; color: var(--muted); padding-left: 2px; }
  .btn { position: absolute; height: 32px; border-radius: 16px; color: var(--white); font-size: 12.5px; display: flex; align-items: center; justify-content: center; width: 118px; }
  .btn-message { left: 675px; top: 318px; background: var(--blue); }
  .btn-review { left: 809px; top: 320px; background: var(--orange); }
  .member-meta { position: absolute; right: 257px; top: 366px; text-align: right; font-family: "Nunito", sans-serif; font-size: 11.5px; line-height: 15px; color: #6a6a70; }

  .profile-facts { position: absolute; left: 256px; top: 506px; width: 300px; list-style: none; }
  .fact { position: relative; height: 40px; display: flex; align-items: center; font-size: 14.5px; }
  .fact::after { content: ""; position: absolute; left: 0; bottom: 0; width: 256px; height: 1px; background: var(--line); }
  .fact:last-child::after { display: none; }
  .fact-label { width: 129px; }
  .fact-value { background: var(--pill-bg); border-radius: 15px; height: 30px; min-width: 83px; padding: 0 22px; display: flex; align-items: center; justify-content: center; color: #66666b; font-size: 15px; }

  .rates { position: absolute; left: 256px; top: 781px; border-collapse: collapse; font-size: 12px; }
  .rates th { background: var(--blue); color: var(--white); font-weight: normal; height: 23px; width: 68px; border-right: 1px solid var(--white); }
  .rates th.subject-head, .rates td.subject { background: var(--orange); color: var(--white); width: 104px; text-align: left; padding-left: 9px; }
  .rates td { height: 21px; text-align: center; border: 1px solid var(--line); color: #555; }
  .rates td.subject { border: none; border-top: 1px solid #f9b05a; }

  .site-footer { position: absolute; left: 0; top: 926px; width: 1200px; height: 45px; background: var(--footer-bg); color: #d8d8dc; font-family: "Nunito", sans-serif; font-size: 13px; display: flex; align-items: center; justify-content: center; }
</style>
</head>
<body>
  <header class="site-header">
    <div class="brand"><span class="brand-dot"></span><span class="brand-name">LendYourLessons</span></div>
    <div class="account-links">Register<span>|</span>Login</div>
    <nav class="main-nav"><span>Home</span><span>Student</span><span>Tutor</span><span>About</span><span>Contact</span></nav>
    <div class="search-box">
      <svg width="11" height="11" viewBox="0 0 11 11"><circle cx="4.5" cy="4.5" r="3.5" fill="none" stroke="#c8c8ce" stroke-width="1.3"/><line x1="7" y1="7" x2="10" y2="10" stroke="#c8c8ce" stroke-width="1.3"/></svg>
      search
    </div>
  </header>

  <section class="hero">
    <div class="hero-ring"></div>
    <div class="hero-photo" role="img" aria-label="Portrait photo of the tutor, a smiling young man in a denim shirt"></div>
    <div class="accent-circle"></div>
    <div class="intro-card">
      <h1 class="intro-title">Hello, my name is Oliver and I am a tutor</h1>
      <p class="intro-text">Lorem ipsum dolor sit amet, consectetur adipiscing elit, sed do eiusmod tempor incididunt ut labore et dolore magna aliqua. Ut enim ad minim veniam, quis nostrud exercitation ullamco laboris nisi ut aliquip ex ea commodo consequat. Duis aute irure dolor in reprehenderit</p>
    </div>
    <div class="btn btn-message">Send mesage</div>
    <div class="btn btn-review">Write review</div>
    <div class="member-meta">Member since: Jun 13, 2015<br>Last Logged In : May 22, 2016 11:22 PM</div>
  </section>

  <ul class="profile-facts">
    <li class="fact"><span class="fact-label">Review Score</span><span class="fact-value">4.5/5</span></li>
    <li class="fact"><span class="fact-label">Reliability</span><span class="fact-value">4.0/5</span></li>
    <li class="fact"><span class="fact-label">Punctuality</span><span class="fact-value">4.6/5</span></li>
    <li class="fact"><span class="fact-label">Tutoring Type</span><span class="fact-value">In personal only</span></li>
    <li class="fact"><span class="fact-label">Willing to travel</span><span class="fact-value">Home only</span></li>
    <li class="fact"><span class="fact-label">Age</span><span class="fact-value">20</span></li>
  </ul>

  <table class="rates">
    <tr><th class="subject-head">Subject Taught</th><th>Primary</th><th>Secondary</th><th>GCSE</th><th>A-LEVEL</th><th>University</th><th>Adult Learner</th></tr>
    <tr><td class="subject">Bology</td><td>£20</td><td></td><td>£25</td><td>£30</td><td></td><td></td></tr>
    <tr><td class="subject">Chemistry</td><td>£20</td><td></td><td>£25</td><td>£30</td><td></td><td></td></tr>
  </table>

  <footer class="site-footer">Copyright © 2016&nbsp; Lend Your Lessons. All rights reserved</footer>
</body>
</html>
```